Geschäftspapiere für Lasergravuren
Zielgruppe
Lasergravuren z.B. auf Glas, Holz, Filz, Papier, Acryl, eloxierten Aluminium zu Dekorationszwecken,
Ausschneiden von Elementen z.B. aus Holz, Filz, Papier, Acryl usw. zu Dekorationszwecken mit dem Lasergravierer.
Anfertigung verschiedener Dekorationsartikel,
Zielgruppe: Frauen (mit Familien) aller Altersgruppen, die Freude am Dekorieren und Verschenken haben
Aufgabenstellung
Das vorhandene Logo soll mit eingebunden werden

```html
<!DOCTYPE html>
<html lang="de">
<head>
<meta charset="utf-8">
<title>Lumavio – Briefbogen</title>
<link rel="stylesheet" href="https://fonts.googleapis.com/css2?family=Arimo:wght@400&display=swap">
<style>
  :root {
    --backdrop: #f6f6f6;
    --paper: #ffffff;
    --band-grey: #737478;
    --gold: #a87f4f;
    --ink: #6d6e71;
  }
  * { margin: 0; padding: 0; box-sizing: border-box; }
  html, body { width: 1200px; height: 1200px; overflow: hidden; }
  body { background: var(--backdrop); font-family: "Arimo", Arial, sans-serif; color: var(--ink); }

  .letterhead {
    position: absolute; left: 282px; top: 151px;
    width: 635px; height: 898px;
    background: var(--paper);
    border: 1px solid #e2e2e2;
  }
  .top-band { position: absolute; left: 0; top: 0; width: 100%; height: 11px; background: var(--band-grey); }

  .brand { position: absolute; left: 424px; top: 34px; width: 160px; text-align: center; }
  .brand-mark { display: block; margin: 0 auto 8px; }
  .brand-name { font-size: 38px; line-height: 1; font-weight: 400; color: var(--band-grey); letter-spacing: 1px; }

  .sender-line { position: absolute; left: 68px; top: 145px; font-size: 8px; white-space: nowrap; }

  .contact-list { position: absolute; left: 442px; top: 144px; list-style: none; }
  .contact-list li { display: flex; align-items: center; height: 15px; font-size: 10px; }
  .contact-list svg { width: 9px; height: 9px; margin-right: 6px; fill: var(--gold); }
  .contact-list .sep { margin-right: 5px; }

  .legal-col {
    position: absolute; top: 816px; height: 44px;
    border-left: 2px solid var(--gold);
    padding-left: 10px; padding-top: 2px;
    font-size: 10.5px; line-height: 12.8px;
  }
  .legal-seat { left: 68px; }
  .legal-bank { left: 236px; }
  .legal-register { left: 459px; }

  .bottom-band { position: absolute; left: 0; top: 870px; width: 635px; height: 11px; }
</style>
</head>
<body>
  <main class="letterhead">
    <div class="top-band"></div>

    <div class="brand">
      <svg class="brand-mark" width="48" height="48" viewBox="0 0 48 48" aria-hidden="true">
        <circle cx="24" cy="24" r="22" fill="none" stroke="var(--gold)" stroke-width="1.2"/>
      </svg>
      <div class="brand-name">Lumavio</div>
    </div>

    <p class="sender-line">Company (Haftungsbeschränkt) | 123 Your Street, Your Suburb and State</p>

    <ul class="contact-list">
      <li><svg viewBox="0 0 10 10"><path d="M2 0.5l2 2-1 1.2c.6 1.3 1.5 2.2 2.8 2.8l1.2-1 2 2-1.3 1.8C4 9 1 6 .3 1.8z"/></svg><span class="sep">|</span>0000 (0)11 222 333 44</li>
      <li><svg viewBox="0 0 10 10"><rect x="2.5" y="0.5" width="5" height="2.5"/><rect x="0.5" y="3.5" width="9" height="4" rx="1"/><rect x="2.5" y="6" width="5" height="3.5" fill="#fff" stroke="var(--gold)" stroke-width=".8"/></svg><span class="sep">|</span>0000 (0)11 555 666 77</li>
      <li><svg viewBox="0 0 10 10"><circle cx="5" cy="5" r="4.3" fill="none" stroke="var(--gold)" stroke-width=".9"/><ellipse cx="5" cy="5" rx="1.8" ry="4.3" fill="none" stroke="var(--gold)" stroke-width=".8"/><path d="M.7 5h8.6M1.5 2.8h7M1.5 7.2h7" stroke="var(--gold)" stroke-width=".7"/></svg><span class="sep">|</span>www.company.com</li>
      <li><svg viewBox="0 0 10 10"><rect x="0.5" y="2" width="9" height="6"/><path d="M.5 2l4.5 3.5L9.5 2M.5 8l3.3-3M9.5 8L6.2 5" stroke="#fff" stroke-width=".8" fill="none"/></svg><span class="sep">|</span>info@company.com</li>
    </ul>

    <div class="legal-col legal-seat">Sitz der Gesellschaft<br>Geschäftsführer</div>
    <div class="legal-col legal-bank">Bank: Bank<br>IBAN: 0000 0000 000 0000 0000<br>BIC: 00000000000</div>
    <div class="legal-col legal-register">Handelsregister<br>Umsatzsteuer id</div>

    <svg class="bottom-band" viewBox="0 0 635 11" aria-hidden="true">
      <polygon points="0,0 450,0 439,11 0,11" fill="var(--gold)"/>
      <polygon points="459,0 477,0 466,11 448,11" fill="var(--band-grey)"/>
      <polygon points="486,0 635,0 635,11 475,11" fill="var(--gold)"/>
    </svg>
  </main>
</body>
</html>
```